Verdell Chiropractic, achieve your health goals, get better each day one step at a time

A mobile friendly site, fresh look, easy to navigate, has interface with pw/chirply, etc. Blog posts. Uses new logo. Content and address to current site is mirvaton.com. The current site will give you scope of project for content. The logo is not the final but close. Will upload final next week.
Convey the concept that heath is a process, it does not just happen. We take steps to achieve what we want in life including health.

Target Market(s)

30 to 70 year old. Needing health care

Industry/Entity Type

Health Care

Coding

Coded - Design and coding required

Number of Pages Required

5+ page

Font styles to use
Sans Serif

Colors

Designer to choose colors to be used in the design.

Requirements
Must have
• mobile friendly, easy to navigate, PW/Chirply interface, blog, room for current content
Nice to have
• potential for commerce, statistics
Should not have
• Same old look and feel as everything else out there

```html
<!DOCTYPE html>
<html lang="en">
<head>
<meta charset="utf-8">
<title>Meet Dr. Marlow – Verdell Chiropractic</title>
<link rel="stylesheet" href="https://fonts.googleapis.com/css2?family=Mulish:wght@300;400;600;700&display=swap">
<style>
  :root {
    --brand-blue: #2f7bbd;
    --brand-green: #8cc152;
    --text-dark: #3a3a3a;
    --nav-text: #4a4a4a;
    --white: #ffffff;
    --footer-bg: #4b4b50;
    --page-bg: #ffffff;
  }
  * { box-sizing: border-box; margin: 0; padding: 0; }
  html, body {
    width: 1152px; height: 1200px; overflow: hidden;
    background: var(--page-bg);
    font-family: "Mulish", sans-serif;
    color: var(--text-dark);
  }
  .page { position: relative; width: 1152px; height: 1200px; overflow: hidden; }

  .site-header {
    position: absolute; left: 0; top: 0; width: 1152px; height: 74px;
    background: var(--white);
    box-shadow: 0 1px 3px rgba(0,0,0,.08);
    z-index: 2;
  }
  .brand {
    position: absolute; left: 150px; top: 24px;
    display: flex; align-items: center; gap: 7px;
    font-weight: 700; font-size: 15px; color: var(--brand-blue);
    letter-spacing: .2px;
  }
  .brand-mark { width: 12px; height: 12px; background: var(--brand-blue); }
  .main-nav {
    position: absolute; left: 425px; top: 26px;
    display: flex; gap: 27px;
    font-size: 11px; color: var(--nav-text); font-weight: 400;
  }
  .btn-appointment {
    position: absolute; left: 857px; top: 18px; width: 142px; height: 31px;
    border-radius: 16px; background: var(--brand-blue); color: var(--white);
    font-size: 11px; display: flex; align-items: center; justify-content: center;
  }

  .hero {
    position: absolute; left: 0; top: 74px; width: 1152px; height: 214px;
    background: linear-gradient(90deg, #7fa9cf 0%, #8db9c7 45%, #a7cc96 80%, #b8d68a 100%);
  }
  .hero-title {
    position: absolute; left: 0; top: 84px; width: 100%;
    text-align: center; color: var(--white);
    font-weight: 300; font-size: 30px; letter-spacing: .5px;
  }

  .portrait {
    position: absolute; left: 122px; top: 383px; width: 428px; height: 570px;
    border-radius: 8px;
    background: linear-gradient(160deg, #d7c2a4 0%, #c9a584 40%, #5a4a40 75%, #2e2a2c 100%);
  }

  .bio { position: absolute; left: 584px; top: 0; width: 440px; }
  .bio h2 {
    position: absolute; left: 0; white-space: nowrap;
    font-weight: 400; font-size: 24px; color: var(--brand-blue);
    letter-spacing: .3px;
  }
  .bio ul { position: absolute; left: 1px; list-style: none; width: 440px; }
  .bio li {
    font-size: 12px; line-height: 18px; text-transform: uppercase;
    margin-bottom: 5px; color: var(--text-dark);
  }

  .site-footer {
    position: absolute; left: 0; top: 1069px; width: 1152px; height: 131px;
    background: var(--footer-bg); color: var(--white);
  }
  .footer-col { position: absolute; top: 86px; }
  .footer-col h3 { font-weight: 400; font-size: 16px; letter-spacing: .3px; }
  .footer-col p { font-size: 11px; margin-top: 12px; opacity: .9; }
  .footer-about { left: 164px; }
  .footer-links { left: 537px; text-align: center; width: 80px; }
  .footer-contact { left: 880px; text-align: center; width: 118px; }
</style>
</head>
<body>
<div class="page">
  <header class="site-header">
    <div class="brand"><span class="brand-mark"></span>Verdell Chiropractic</div>
    <nav class="main-nav">
      <span>Home</span><span>Meet Dr. Marlow</span><span>Testimonials</span><span>Faqs</span><span>Resources</span><span>Contact</span>
    </nav>
    <div class="btn-appointment">Make an Appointment</div>
  </header>

  <section class="hero" role="img" aria-label="Treatment room with patient chairs, tinted blue to green">
    <h1 class="hero-title">MEET DR. MARLOW</h1>
  </section>

  <div class="portrait" role="img" aria-label="Photo of the doctor and his wife standing by a brick wall"></div>

  <section class="bio">
    <h2 style="top:374px">EDUCATION</h2>
    <ul style="top:420px">
      <li>Lone Ridge Chiropractic College 1991, Doctor of Chiropractic with honors</li>
    </ul>

    <h2 style="top:482px;left:2px">ADDITIONAL EDUCATION</h2>
    <ul style="top:527px">
      <li>Diplomate, Allied Board of Homeopathic Examiners, 1991</li>
      <li>Diplomate, Chiropractic Council of Clinical Nutritionists, 1996</li>
      <li>Certified, Clinical Nutritionist, Continental Academy of Clinical Nutrition, 1996</li>
      <li>Certified, Acupuncture, Lone Ridge Chiropractic College, 1999</li>
      <li>Certified, Global Academy of Applied Kinesiology, 2004</li>
      <li>Allied Board of Chiropractic Internists&nbsp; 180 hours</li>
      <li>Allied Board of Chiropractic Neurology&nbsp; 100 hours</li>
      <li>Advanced Kinesiology, Arlen Pike DC,&nbsp; 60 hours</li>
      <li>Advanced Kinesiology, Nora Vassel DO,&nbsp; 60 hours</li>
    </ul>

    <h2 style="top:785px;left:-1px">LICENSURE</h2>
    <ul style="top:830px">
      <li>Southplains Board of Chiropractic Examiners</li>
      <li>&nbsp;Mesa Valley Board of Chiropractic Examiners</li>
    </ul>

    <h2 style="top:912px">MEMBER</h2>
    <ul style="top:955px">
      <li>Southplains Chiropractic Association</li>
    </ul>
  </section>

  <footer class="site-footer">
    <div class="footer-col footer-about">
      <h3>DANIEL MARLOW</h3>
      <p>Lorem Ipsum is simply dummy text of</p>
    </div>
    <div class="footer-col footer-links">
      <h3>SITE LINKS</h3>
      <p>Home</p>
    </div>
    <div class="footer-col footer-contact">
      <h3>CONATCT US</h3>
      <p>Daniel Marlow DC PA</p>
    </div>
  </footer>
</div>
</body>
</html>
```